Tenth Annual Silverfern Ivory Carnival Soiree to Benefit Tidewell Ledger Circle Foundation

Date: 2 February 2024
Location: The Halcrest Pelican Shoals Coral Bay Resort & Spa
Time: Doors open 5:00pm
Attire: White Elegance (a variety of masks will be available at the extravaganza)

Target Market(s)

Early to mid career men and women (aged 25-40)

Industry/Entity Type

Financial Services / Asset Management

Font styles to use
Serif

Colors
0054AA
0677BA
7BADD7
CADEEF
E8F1F8
00AB8E
00BBA5
67D7C9
C6EFE9
E9F9F6
59FF00
82FF00
B8FF75
E3FFCB
F4FFEA

Requirements
Must have
• Masquerade images. The event is being held on the beach in the Caribbean.

```html
<!DOCTYPE html>
<html lang="en">
<head>
<meta charset="utf-8">
<title>Silverfern Ivory Carnival Soiree</title>
<link rel="stylesheet" href="https://fonts.googleapis.com/css2?family=Great+Vibes&family=Playfair+Display:wght@600;700;800&family=Oswald:wght@500&family=Montserrat:wght@500;600&display=swap">
<style>
  :root {
    --stage: #e9e9ef;
    --night: #07072a;
    --royal: #1c1fb5;
    --gold: #e8c468;
    --gold-light: #f3d98c;
    --gold-deep: #c99a3c;
    --silver: #e4e4ea;
    --ink: #0b0b35;
    --lime: #59ff00;
    --mask-green: #5f8f4a;
    --flame: #d8541a;
    --sea: #0677ba;
    --sand: #c9a46a;
    --white: #ffffff;
  }
  * { margin: 0; padding: 0; box-sizing: border-box; }
  html, body { width: 1200px; height: 900px; overflow: hidden; background: var(--stage); }
  .canvas { position: relative; width: 1200px; height: 900px; }
  .flyer {
    position: absolute; left: 290px; top: 12px; width: 620px; height: 876px; overflow: hidden;
    background: linear-gradient(180deg, var(--night) 0%, #12127a 62%, var(--royal) 82%, #0d0d5a 100%);
  }
  .hero-photo {
    position: absolute; left: 0; top: 0; width: 620px; height: 560px;
    background:
      radial-gradient(ellipse 40% 36% at 46% 30%, var(--mask-green) 0%, rgba(60,100,50,0.6) 45%, rgba(0,0,0,0) 75%),
      radial-gradient(ellipse 38% 42% at 80% 36%, var(--flame) 0%, rgba(180,40,10,0.7) 40%, rgba(0,0,0,0) 75%),
      radial-gradient(ellipse 32% 38% at 18% 52%, #b83a12 0%, rgba(120,20,10,0.5) 45%, rgba(0,0,0,0) 75%),
      radial-gradient(ellipse 26% 18% at 78% 62%, rgba(230,230,240,0.55) 0%, rgba(0,0,0,0) 75%),
      radial-gradient(ellipse 24% 16% at 22% 74%, rgba(232,196,104,0.55) 0%, rgba(0,0,0,0) 75%),
      linear-gradient(180deg, #050510 0%, #0b0b30 58%, rgba(6,119,186,0.35) 74%, rgba(201,164,106,0.18) 84%, rgba(10,10,60,0) 100%);
  }
  .brand {
    position: absolute; left: 0; right: 0; top: 430px;
    display: flex; align-items: center; justify-content: center; gap: 10px;
  }
  .brand-dot { width: 22px; height: 22px; border-radius: 50%; background: var(--lime); }
  .brand-name { font-family: "Playfair Display", serif; font-weight: 700; font-size: 20px; color: var(--white); }
  .presents {
    position: absolute; left: 0; right: 0; top: 462px; text-align: center;
    font-family: "Montserrat", sans-serif; font-weight: 500; font-size: 15px; letter-spacing: 3px; color: var(--white);
  }
  .title-script {
    position: absolute; left: 0; right: 0; top: 482px; text-align: center;
    font-family: "Great Vibes", cursive; font-weight: 400; font-size: 90px; line-height: 1; color: var(--silver);
    text-shadow: 0 2px 6px rgba(0,0,0,0.6);
  }
  .title-pill {
    position: absolute; left: 110px; width: 400px; top: 606px; height: 48px; border-radius: 24px;
    background: linear-gradient(180deg, var(--gold-light), var(--gold-deep));
    display: flex; align-items: center; justify-content: center;
    font-family: "Playfair Display", serif; font-weight: 800; font-size: 29px; letter-spacing: 2px; color: var(--ink);
  }
  .details { position: absolute; left: 30px; right: 30px; top: 668px; height: 98px; display: flex; align-items: center; }
  .detail { flex: 1; text-align: center; }
  .detail + .detail { border-left: 1px solid rgba(255,255,255,0.5); }
  .gold-serif { font-family: "Playfair Display", serif; font-weight: 700; color: var(--gold); line-height: 1; }
  .small-line { font-size: 20px; }
  .big-line { font-size: 46px; }
  .label-pill {
    display: inline-block; padding: 2px 12px; border-radius: 10px; background: #d5d5dc;
    font-family: "Montserrat", sans-serif; font-weight: 600; font-size: 12px; letter-spacing: 2px; color: var(--ink);
  }
  .address {
    margin-top: 6px; font-family: "Oswald", sans-serif; font-weight: 500; font-size: 14px; line-height: 1.15;
    color: var(--white); text-transform: uppercase;
  }
  .attire { position: absolute; left: 0; right: 0; top: 778px; text-align: center; }
  .attire-value {
    margin-top: 4px; font-family: "Playfair Display", serif; font-weight: 800; font-size: 32px; line-height: 1.1;
    letter-spacing: 2px; color: var(--gold);
  }
  .note-pill {
    position: absolute; left: 40px; right: 40px; top: 842px; height: 22px; border-radius: 11px;
    background: linear-gradient(180deg, var(--gold-light), var(--gold-deep));
    display: flex; align-items: center; justify-content: center;
    font-family: "Montserrat", sans-serif; font-weight: 600; font-size: 11.5px; letter-spacing: 1px; color: var(--ink);
  }
</style>
</head>
<body>
<main class="canvas">
  <article class="flyer">
    <div class="hero-photo" role="img" aria-label="Masquerade scene: a guest in an ornate venetian mask with gold and silver carnival masks, fiery glow and gold confetti over a moonlit Caribbean beach"></div>

    <div class="brand">
      <span class="brand-dot"></span>
      <span class="brand-name">Tidewell Ledger Circle Foundation</span>
    </div>
    <p class="presents">PRESENTS</p>

    <h1 class="title-script">Silverfern Ivory</h1>
    <div class="title-pill">CARNIVAL SOIREE</div>

    <section class="details">
      <div class="detail">
        <div class="gold-serif small-line">DOOR</div>
        <div class="gold-serif big-line">5PM</div>
        <div class="gold-serif small-line">OPEN</div>
      </div>
      <div class="detail">
        <span class="label-pill">LOCATION</span>
        <p class="address">The Halcrest Pelican Shoals<br>Coral Bay Resort &amp; Spa</p>
      </div>
      <div class="detail">
        <div class="gold-serif small-line">FEB</div>
        <div class="gold-serif big-line">2</div>
        <div class="gold-serif small-line">FRI</div>
      </div>
    </section>

    <section class="attire">
      <span class="label-pill">ATTIRE</span>
      <p class="attire-value">WHITE ELEGANCE</p>
    </section>
    <p class="note-pill">(A VARIETY OF MASKS WILL BE AVAILABLE AT THE EXTRAVAGANZA)</p>
  </article>
</main>
</body>
</html>
```